Redesign vek7.ch agency website for unique design with speed and conversion

We want to redesign our website vek7.ch. Our omnichannel marketing agency builds webshops and integrates them into existing systems like ERP/CRM and supports with online marketing campaigns like plimtor ads and social media. The target of the redesign is to get a great look and feel for customers to see directly what we do, (please design something for our three focus areas eCommerce, Online marketing and Integration)
and to improve the pages speed drastically for SEO. Please see our attachment.
Target Market(s)
B2B
Industry/Entity Type
eCommerce Agency
Coding
Coded - Design and coding required
Number of Pages Required
5+ page
Look and feel
Each slider illustrates characteristics of the customer's brand and the style your logo design should communicate.

```html
<!DOCTYPE html>
<html lang="de">
<head>
<meta charset="utf-8">
<title>vek7 – Online Marketing Agentur in Zürich</title>
<link href="https://fonts.googleapis.com/css2?family=Montserrat:wght@600;700&family=Roboto:wght@400&display=swap" rel="stylesheet">
<style>
  :root {
    --brand-green: #4be35b;
    --ink: #2b3036;
    --ink-soft: #3a3f45;
    --bg-light: #f7f7f6;
    --bg-mid: #e9ebec;
    --bg-warm: #efe9e2;
    --white: #ffffff;
  }
  * { margin: 0; padding: 0; box-sizing: border-box; }
  html, body {
    width: 1200px;
    height: 614px;
    overflow: hidden;
    background: var(--white);
  }
  .hero {
    position: relative;
    width: 1200px;
    height: 614px;
    overflow: hidden;
    font-family: "Montserrat", sans-serif;
    color: var(--ink);
  }
  .hero-backdrop {
    position: absolute;
    inset: 0;
    background:
      radial-gradient(ellipse 420px 260px at 760px 160px, rgba(200,210,220,0.55), transparent 70%),
      radial-gradient(ellipse 380px 300px at 1080px 380px, rgba(225,228,232,0.7), transparent 70%),
      radial-gradient(ellipse 300px 200px at 1150px 80px, rgba(236,205,150,0.35), transparent 70%),
      linear-gradient(100deg, var(--bg-light) 0%, var(--bg-light) 35%, var(--bg-mid) 70%, var(--bg-warm) 100%);
  }
  .brand {
    position: absolute;
    left: 71px;
    top: 22px;
    font-family: "Montserrat", sans-serif;
    font-weight: 700;
    font-size: 42px;
    line-height: 50px;
    letter-spacing: 1px;
    color: var(--brand-green);
    text-decoration: none;
  }
  .main-nav a {
    position: absolute;
    top: 38px;
    font-weight: 700;
    font-size: 13.5px;
    line-height: 16px;
    letter-spacing: 0.2px;
    color: var(--ink);
    text-decoration: none;
    text-transform: uppercase;
    white-space: nowrap;
  }
  .main-nav .is-active::after {
    content: "";
    position: absolute;
    left: 0;
    right: 0;
    top: 30px;
    height: 4px;
    background: var(--brand-green);
  }
  .nav-dropdown { display: inline-flex; align-items: center; gap: 4px; }
  .nav-dropdown svg { width: 16px; height: 10px; }
  .hero-title {
    position: absolute;
    left: 0;
    right: 0;
    top: 192px;
    text-align: center;
    font-weight: 700;
    font-size: 55px;
    line-height: 81px;
    color: var(--ink);
  }
  .hero-lead {
    position: absolute;
    left: 290px;
    width: 620px;
    top: 376px;
    text-align: center;
    font-family: "Roboto", sans-serif;
    font-size: 16.5px;
    line-height: 26px;
    color: var(--ink-soft);
  }
  .hero-actions {
    position: absolute;
    top: 480px;
    left: 421px;
    display: flex;
    gap: 26px;
  }
  .btn {
    display: flex;
    align-items: center;
    justify-content: center;
    width: 166px;
    height: 48px;
    font-weight: 700;
    font-size: 14px;
    letter-spacing: 0.3px;
    text-transform: uppercase;
    text-decoration: none;
  }
  .btn-primary { background: var(--brand-green); color: var(--white); }
  .btn-outline { border: 3px solid var(--ink); color: var(--ink); }
</style>
</head>
<body>
  <section class="hero">
    <div class="hero-backdrop" role="img" aria-label="Softly faded photo of a desk with a laptop showing sales charts and a world map, hands pointing at the screen and writing on printed reports"></div>

    <a class="brand" href="#">vek7</a>

    <nav class="main-nav">
      <a class="is-active" href="#" style="left:422px">Home</a>
      <a href="#" style="left:507px">Webshop</a>
      <a href="#" style="left:625px">Plimtor Ads</a>
      <a href="#" style="left:764px">SEO</a>
      <a href="#" style="left:833px">Social Media Marketing</a>
      <a class="nav-dropdown" href="#" style="left:1077px">VEK7
        <svg viewBox="0 0 16 10" aria-hidden="true"><path d="M1.5 1.5 L8 8 L14.5 1.5" fill="none" stroke="currentColor" stroke-width="2.2"/></svg>
      </a>
    </nav>

    <h1 class="hero-title">Ihre Online Marketing Agentur<br>in Zürich für KMUs</h1>

    <p class="hero-lead">Sie möchten Online die richtigen Menschen erreichen und mehr Umsatz generieren. Kontaktieren Sie uns!</p>

    <div class="hero-actions">
      <a class="btn btn-primary" href="#">Offerte</a>
      <a class="btn btn-outline" href="#">Termin</a>
    </div>
  </section>
</body>
</html>
```